Quill Harbor Gems Website revamp

Hi,

We need a working WordPress theme, not just a .PSD file. Thank you.

We need a complete revamp of our website. We sell lab grown diamonds online. We sell the idea that everyone should be able to afford a diamond. Thus our diamonds are priced very reasonably. Our selling point "the joy of giving and receiving a diamond in a little box".

Our range of products includes rings, bangles, necklace, ear rings etc. We currently only operate in Singapore. Some photos of our products are on our websites.

Need.
- Clean look and feel, simplistic preferably white and soft colours
- Easy to navigate
- No banners
- E Com
- Introduction page
- Willing to change logo if needed

Existing page: www.quillharborgems-example.com

Target Market(s)

Young ladies
Ladies
Men buying for ladies
Young boyfriends fresh out of school buying for love ones
Working ladies to match what they wear to work

Industry/Entity Type

Online

Requirements
Must have
• ECOM. Product shopping cart
Pictures uploads
Intro page
Nice to have
• Pastel colors preferred. - Color scheme is important in our business to create a long term impression. Color scheme will also be used for next potential project, i.e. packaging design.

Should not have
• Should not have old style fonts.

```html
<!DOCTYPE html>
<html lang="en">
<head>
<meta charset="utf-8">
<title>Quill Harbor Gems</title>
<link rel="stylesheet" href="https://fonts.googleapis.com/css2?family=Ubuntu:wght@300;400&family=Ubuntu+Condensed&family=PT+Serif&display=swap">
<style>
:root{
  --bg-top:#f3f1ec;
  --page:#ffffff;
  --teal:#45c2b6;
  --brown:#6b5f4f;
  --ink:#4d4a45;
  --muted:#a7a4a0;
  --line:#dcdad6;
  --pink:#e46cc0;
  --gold:#e2a233;
  --footer:#f8f8f7;
}
*{box-sizing:border-box;margin:0;padding:0}
html,body{width:1165px;height:1200px;overflow:hidden}
body{position:relative;background:var(--page);font-family:"Ubuntu",sans-serif;font-weight:300;color:var(--ink)}
.top-band{position:absolute;left:0;top:0;width:1165px;height:420px;background:var(--bg-top);border-top:4px solid #e2e0dc}
.brand{position:absolute;left:138px;top:86px;display:flex;align-items:center;gap:10px;font-size:24px;font-weight:300;color:#9a9487}
.brand-mark{width:18px;height:18px;border:2px solid #9a9487}
.util-nav{position:absolute;right:127px;top:18px;font-size:12px;font-weight:400;color:#3e3a35;white-space:nowrap}
.util-nav span{margin:0 6px;color:#777}
.search{position:absolute;left:797px;top:96px;width:241px;height:32px;background:#fff;border:1px solid #e1dfdb;display:flex;align-items:center;padding-left:8px;gap:7px;font-size:12px;color:#888}
.main-nav{position:absolute;left:120px;top:141px;width:920px;height:46px;background:linear-gradient(#56cec2,#3fbfb2);border-radius:3px 3px 0 0;display:flex}
.main-nav a{font-family:"Ubuntu Condensed","Ubuntu",sans-serif;font-size:15px;color:#fff;text-decoration:none;display:flex;align-items:center;justify-content:center;border-right:1px solid #36a99d;white-space:nowrap}
.hero{position:absolute;left:120px;top:187px;width:920px;height:355px;background:#fff;border:1px solid var(--line);border-top:none;border-radius:0 0 4px 4px}
.hero-kicker{position:absolute;left:62px;top:86px;font-size:32px;line-height:36px;font-weight:300;color:var(--teal);white-space:nowrap}
.hero-title{position:absolute;left:61px;top:118px;font-size:43px;line-height:50px;font-weight:400;color:var(--brown);white-space:nowrap}
.hero-text{position:absolute;left:62px;top:178px;width:340px;font-size:12px;line-height:19.8px;color:var(--muted)}
.dots{position:absolute;left:62px;top:254px;display:flex;gap:4px}
.dots i{width:11px;height:11px;border-radius:50%;background:#e2e2e2}
.dots i:first-child{background:#5cb8d0}
.hero-photo{position:absolute;left:469px;top:42px;width:346px;height:279px;border-radius:40%;background:radial-gradient(circle,#e6e8ea 0%,#f4f5f6 55%,#fff 75%)}
.card{position:absolute;top:557px;width:299px;height:148px;border:1px solid var(--line);border-radius:3px;background:linear-gradient(#fff,#f6f5f2)}
.card h3{position:absolute;left:20px;top:20px;font-size:20px;line-height:26px;font-weight:300;white-space:nowrap;z-index:1}
.card p{position:absolute;left:22px;top:56px;width:150px;font-size:11px;line-height:16px;color:#5a5650}
.card .more{position:absolute;left:23px;top:114px;font-size:12.5px;line-height:16px;font-weight:400;color:#3f3b36}
.card .thumb{position:absolute;right:14px;top:40px;width:92px;height:98px;border-radius:8px}
.card-specials{left:121px}.card-specials h3{color:var(--pink)}
.card-diamond{left:430px}.card-diamond h3{color:var(--gold)}
.card-box{left:738px}.card-box h3{color:var(--teal)}
.about{position:absolute;left:123px;top:743px;width:610px}
.about h2{font-family:"PT Serif",serif;font-weight:400;font-size:23px;line-height:30px;color:#3f3b36;margin-bottom:8px}
.about p{font-size:11.8px;line-height:19.8px;color:#4d4a45;margin-bottom:19.8px}
.contact{position:absolute;left:784px;top:742px;width:259px;height:289px;background:var(--bg-top);border-radius:3px}
.contact h2{position:absolute;left:22px;top:14px;font-family:"PT Serif",serif;font-weight:400;font-size:20px;line-height:26px;color:#2f2c28;white-space:nowrap}
.contact .sub{position:absolute;left:22px;top:44px;font-size:10.5px;line-height:14px;color:#3f3b36;white-space:nowrap}
.fields{position:absolute;left:20px;top:72px}
.field{width:220px;height:27px;background:#fff;border:1px solid #dcdad5;margin-bottom:6px;font-size:11px;line-height:14px;color:#888;padding:6px 11px}
.field.msg{height:58px}
.submit{position:absolute;left:159px;top:241px;width:82px;height:27px;background:linear-gradient(#4fcabd,#33b3a6);border-radius:3px;color:#fff;font-family:"Ubuntu Condensed","Ubuntu",sans-serif;font-size:14px;display:flex;align-items:center;justify-content:center}
.footer{position:absolute;left:0;top:1110px;width:1165px;height:90px;background:var(--footer);box-shadow:0 -3px 6px rgba(0,0,0,.05)}
.footer p{position:absolute;left:130px;top:28px;font-size:12.5px;color:#6b6862}
.social{position:absolute;left:933px;top:27px;display:flex;gap:7px}
.social i{width:20px;height:20px;border-radius:2px}
</style>
</head>
<body>
<div class="top-band"></div>
<div class="brand"><span class="brand-mark"></span>Quill Harbor Gems</div>
<nav class="util-nav">MY ACCOUNT<span>|</span>LOGIN<span>|</span>CHECKOUT<span>|</span>SUPPORT</nav>
<div class="search">
  <svg width="16" height="16" viewBox="0 0 16 16"><circle cx="6.5" cy="6.5" r="5" fill="none" stroke="#aaa" stroke-width="1.3"/><line x1="10.2" y1="10.2" x2="14.5" y2="14.5" stroke="#aaa" stroke-width="1.3"/></svg>
  Search product
</div>
<nav class="main-nav">
  <a style="width:90px">HOME</a><a style="width:78px">SHOP</a><a style="width:76px">CART</a><a style="width:115px">PRODUCTS</a><a style="width:109px">ABOUT US</a><a style="width:146px">OUR DIAMONDS</a>
</nav>
<section class="hero">
  <div class="hero-kicker">A Perfect Moment</div>
  <h1 class="hero-title">Captured in time..</h1>
  <p class="hero-text">Duis tincidunt lectus quis dui viverra vestibulum. Suspendisse vulputate aliquam dui. Nulla elementum dui ut augue. Aliquam vehicula mi at mauris. Maecenas placerat</p>
  <div class="dots"><i></i><i></i><i></i><i></i></div>
  <div class="hero-photo" role="img" aria-label="Diamond engagement ring with two loose diamonds"></div>
</section>
<article class="card card-specials">
  <h3>What Specials</h3>
  <p>Morbi diam mauris, viverra in, gravida eu mattis in, ante. Morbi eget arcu.</p>
  <div class="more">View More &#9656;</div>
  <div class="thumb" role="img" aria-label="Ring set with pink stone" style="background:radial-gradient(circle,#ddd6e0,#f2f1ef 70%)"></div>
</article>
<article class="card card-diamond">
  <h3>Diamond Product</h3>
  <p>Morbi diam mauris, viverra in, gravida eu mattis in, ante. Morbi eget arcu</p>
  <div class="more">View More &#9656;</div>
  <div class="thumb" role="img" aria-label="Crossover diamond bangle" style="background:radial-gradient(circle,#e2e4e6,#f6f5f2 70%)"></div>
</article>
<article class="card card-box">
  <h3>Featured Box</h3>
  <p>Morbi diam mauris, viverra in, gravida eu mattis in, ante. Morbi eget arcu.</p>
  <div class="more">View More &#9656;</div>
  <div class="thumb" role="img" aria-label="Teal gift box with white ribbon" style="background:linear-gradient(#c9eeea,#49c6b9)"></div>
</article>
<section class="about">
  <h2>Little About Solitaire</h2>
  <p>When Tomas met Mira, Tomas was a poor bloke. Just out of school, embarking on his first job and without a stable pay. Tomas wanted to buy Mira a nice gift for their first Valentine’s day. However, when he walked into an upscale jewellery shop, the prices on the tags of the diamond pieces set him back. He can’t afford any.</p>
  <p>Quill Harbor Gems was started with one simple philosophy; that diamonds should be made available to anyone. No ladies should be denied the joy of receiving a surprise in a little box, because the gents can’t afford it. The joy should not be in the stone alone, the process of choosing, planning a surprise, wrapping are all parts of giving and receiving. This is what drives us at Quill Harbor Gems everyday.</p>
  <p>At Quill Harbor Gems, we are proud to present to you master pieces direct from Antwerp. Our cultured diamonds are created and designed to delight. Our range includes the affordable to the sophisticated. Check out our diamonds in our pages and feel free to contact us anytime for a private viewing of our pieces.</p>
</section>
<section class="contact">
  <h2>Fill Our Contact Form</h2>
  <p class="sub">Please subscribe here for latest news &amp; offers</p>
  <div class="fields">
    <div class="field">Full Name</div>
    <div class="field">Email address</div>
    <div class="field">Phone no.</div>
    <div class="field msg">Message</div>
  </div>
  <div class="submit">SUBMIT</div>
</section>
<footer class="footer">
  <p>© 2013 Company Name.&nbsp; All right reserved.&nbsp; Term of Use</p>
  <div class="social"><i style="background:#3b5b98"></i><i style="background:#4fb4e6"></i><i style="background:#1f6fa8"></i><i style="background:#f08a1c"></i></div>
</footer>
</body>
</html>
```